Renewable Energy company needs a new website

We are renewable energy company that has been operating for 3 years now and require a new website design. We are looking to upgrade our website to be comparable to our competitors. We are not a brick and mortar business so our website does need to be very appealing and convey a sense of authenticity and trust to the consumer. It will also heavily display our current system special and offering etc. The final design needs to be visually appealing in a marketing sense however also needs to convey a high sense of professionalism.

Target Market(s)

Consumers of solar systems for installation on their home or business.

Coding

Coded - Design and coding required

Number of Pages Required

3 page

Font styles to use
Sans Serif

Colors

Designer to choose colors to be used in the design.

Requirements
Must have
• A home page, a page for residential solar systems including the packages we are currently offering and a commercial page for larger installations of solar systems.
• www.torvapower.com.au
Nice to have
• As a template we do like this https://www.bluneklight.com.au/qld/ in terms of design elements and layout of the page.

```html
<!DOCTYPE html>
<html lang="en">
<head>
<meta charset="utf-8">
<title>Torva Power – Solar &amp; Off-Grid Energy Solutions</title>
<link href="https://fonts.googleapis.com/css2?family=Montserrat:wght@400;500;600;700&family=Open+Sans:wght@400;600&display=swap" rel="stylesheet">
<style>
:root{
  --red:#d9262f;
  --red-dark:#b81c25;
  --dark:#262626;
  --darker:#1c1c1c;
  --heading:#222;
  --text:#6b6b6b;
  --light:#f4f4f4;
  --white:#fff;
  --line:#e2e2e2;
}
*{margin:0;padding:0;box-sizing:border-box}
html,body{width:1200px;height:5338px;overflow:hidden}
body{font-family:"Open Sans",Arial,sans-serif;color:var(--text);background:var(--white);position:relative}
h1,h2,h3,h4,.heading{font-family:"Montserrat",Arial,sans-serif;color:var(--heading)}
section,header,footer,nav{position:absolute;left:0;width:1200px}
.abs{position:absolute}
.btn{position:absolute;background:var(--red);color:var(--white);font-family:"Montserrat",sans-serif;font-size:11px;font-weight:600;text-transform:uppercase;letter-spacing:.3px;display:flex;align-items:center;justify-content:center}
.btn.outline{background:var(--white);color:var(--red)}
.photo{position:absolute}

/* top bar */
.top-bar{top:0;height:21px;background:var(--darker);color:#bbb;font-size:9px}
.top-bar .hours{left:93px;top:5px}
.top-bar .follow{left:955px;top:5px;display:flex;gap:6px;align-items:center}
.dot{width:9px;height:9px;border-radius:50%;background:#ddd;display:inline-block}

/* header */
.site-header{top:21px;height:68px;background:var(--dark)}
.brand{left:93px;top:19px;display:flex;align-items:center;gap:9px}
.brand .mark{width:30px;height:30px;background:var(--red)}
.brand .name{font-family:"Montserrat",sans-serif;font-weight:700;font-size:20px;color:var(--white);line-height:1}
.site-header .quote{left:552px;top:20px;width:100px;height:30px}
.contact-item{position:absolute;display:flex;gap:10px;align-items:center;color:var(--white)}
.contact-item .big{font-family:"Montserrat",sans-serif;font-size:18px;line-height:1.1}
.contact-item .small{font-size:9px;color:#aaa}

/* nav */
.main-nav{top:89px;height:31px;background:var(--red);font-family:"Montserrat",sans-serif;font-size:11px;color:var(--white)}
.main-nav span{position:absolute;top:9px}

/* hero */
.hero{top:120px;height:516px}
.hero-photo{inset:0;background:linear-gradient(100deg,#3d4a55 0%,#5b6670 40%,#6f767a 70%,#4b5257 100%)}
.hero-shade{position:absolute;inset:0;background:linear-gradient(90deg,rgba(0,0,0,.1),rgba(0,0,0,.45))}
.quote-form{left:100px;top:4px;width:248px;height:432px;background:var(--red);color:var(--white)}
.quote-form h3{color:var(--white);font-size:13px;text-align:center;background:rgba(0,0,0,.35);padding:10px 0 4px;font-weight:700}
.quote-form .sub{font-size:8px;text-align:center;background:rgba(0,0,0,.35);padding:0 40px 10px;line-height:1.3}
.field{position:absolute;left:10px;width:225px;font-size:10px}
.field .box{margin-top:5px;height:27px;border:1px solid rgba(255,255,255,.7)}
.quote-form .btn{left:10px;top:387px;width:225px;height:27px;color:var(--red)}
.hero-copy{right:95px;top:170px;text-align:right;color:var(--white)}
.hero-copy .kicker{font-family:"Montserrat",sans-serif;font-size:20px;font-weight:400}
.hero-copy h1{color:var(--white);font-size:46px;font-weight:600;line-height:1.15;margin-top:4px}
.hero-copy p{font-size:12.5px;line-height:1.75;width:530px;margin:14px 0 0 auto}

/* welcome */
.welcome{top:636px;height:520px}
.welcome .kicker{left:93px;top:116px;font-family:"Montserrat",sans-serif;font-size:15px;color:var(--heading)}
.welcome h2{left:93px;top:137px;font-size:44px;font-weight:600}
.welcome p{left:93px;top:205px;width:495px;font-size:12.5px;line-height:1.75}
.welcome .btn{left:93px;top:408px;width:102px;height:30px}
.welcome-photo{left:653px;top:104px;width:452px;height:350px;background:linear-gradient(180deg,#7db4e8 0%,#a9cdef 35%,#4b5f7e 60%,#8f8f8f 100%)}

/* service cards */
.services{top:1173px;height:280px}
.card{position:absolute;top:0;width:238px;height:268px;background:var(--white);border:1px solid #f0f0f0;text-align:left}
.card.raised{box-shadow:0 4px 14px rgba(0,0,0,.12)}
.card .c-tl,.card .c-br{position:absolute;width:40px;height:30px;border-color:#555}
.card .c-tl{left:8px;top:8px;border-left:2px solid;border-top:2px solid}
.card .c-br{right:8px;bottom:8px;border-right:2px solid;border-bottom:2px solid}
.card svg{position:absolute;left:99px;top:18px}
.card .label{position:absolute;top:77px;left:0;width:100%;text-align:center;font-size:8.5px;color:var(--red);text-transform:uppercase;font-family:"Montserrat",sans-serif}
.card h3{position:absolute;left:18px;top:108px;width:205px;font-size:18px;font-weight:500;line-height:1.2}
.card p{position:absolute;left:18px;top:163px;width:195px;font-size:9.5px;line-height:1.55}

/* promo banner */
.promo{top:1524px;height:421px;background:linear-gradient(90deg,var(--red-dark),var(--red) 60%)}
.promo-art{left:670px;top:0;width:530px;height:421px;background:linear-gradient(135deg,#d83038 0%,#d83038 25%,#8ccf4a 55%,#b9e37a 100%)}
.promo .kicker{left:93px;top:78px;font-family:"Montserrat",sans-serif;color:var(--white);font-size:15px}
.promo h2{left:93px;top:100px;color:var(--white);font-size:44px;font-weight:600}
.promo p{left:93px;width:470px;color:var(--white);font-size:12.5px;line-height:1.65}
.promo .btn{left:93px;top:308px;width:124px;height:30px}

/* why solar */
.why{top:1945px;height:1179px}
.why .kicker{left:0;width:1200px;text-align:center;top:82px;font-family:"Montserrat",sans-serif;font-size:15px;color:var(--heading)}
.why h2{left:0;width:1200px;text-align:center;top:104px;font-size:44px;font-weight:600}
.reason{position:absolute;width:505px}
.reason svg{display:block;margin-bottom:12px}
.reason .kick{font-family:"Montserrat",sans-serif;font-size:15.5px;color:var(--heading)}
.reason h3{font-size:27px;font-weight:600;margin-top:2px}
.reason p{font-size:12.5px;line-height:1.75;margin-top:16px}

/* plug into the sun */
.plug{top:3124px;height:597px;background:linear-gradient(135deg,#262626 0%,#1e1e1e 60%,#2a2a2a 100%)}
.plug h2{left:93px;top:70px;color:var(--white);font-size:46px;font-weight:600}
.plug p{left:93px;top:140px;width:460px;font-size:12.5px;line-height:1.75;color:#aaa}
.plug .btn{left:93px;top:274px;width:102px;height:30px}

/* articles */
.articles{top:3721px;height:664px}
.article{position:absolute;top:85px;width:492px}
.article .pic{height:297px}
.article h3{font-size:21px;font-weight:500;margin-top:34px;line-height:1.35}
.article p{font-size:12.5px;line-height:1.75;margin-top:16px}

/* testimonials */
.testimonials{top:4385px;height:445px;background:var(--light)}
.testimonials .kicker{left:0;width:1200px;text-align:center;top:78px;font-family:"Montserrat",sans-serif;font-size:15px;color:var(--heading)}
.testimonials h2{left:0;width:1200px;text-align:center;top:100px;font-size:44px;font-weight:600}
.quote{position:absolute;top:183px;width:460px;text-align:center}
.quote .avatar{width:96px;height:96px;margin:0 auto;background:linear-gradient(180deg,#c9c2b9,#8a7c70)}
.quote p{font-size:12.5px;line-height:1.75;margin-top:20px}
.quote .who{font-family:"Montserrat",sans-serif;font-size:14px;color:var(--heading);margin-top:18px;text-transform:uppercase}
.quote .role{font-size:10px;color:#999}

/* partners */
.partners{top:4830px;height:135px;background:var(--white)}
.badge{position:absolute;top:40px;height:56px;background:#d2d2d2}

/* footer */
.site-footer{top:4965px;height:373px;background:var(--dark);color:#bbb;font-size:11px}
.col{position:absolute;top:62px}
.col h4{color:var(--red);font-size:16px;font-weight:500;margin-bottom:14px;text-transform:uppercase}
.col li{list-style:none;line-height:2.6}
.contact-box{left:580px;top:0;width:270px;height:242px;background:var(--red);color:var(--white)}
.contact-box h4{color:var(--white)}
.contact-box .row{display:flex;gap:7px;align-items:flex-start;margin-bottom:26px;line-height:1.5;width:230px}
.copy{left:0;width:1200px;text-align:center;top:310px;font-size:10px;color:#999}
.copy b{color:var(--white);font-weight:600}
</style>
</head>
<body>

<div class="top-bar" style="position:absolute;left:0;width:1200px;top:0">
  <span class="abs hours">Opening Times: <span style="color:#fff">Monday - Friday: 9:00AM - 5:00PM</span></span>
  <span class="abs follow">Follow Us On <i class="dot"></i><i class="dot"></i><i class="dot"></i><i class="dot"></i></span>
</div>

<header class="site-header">
  <div class="abs brand">
    <span class="mark"></span>
    <span class="name">TORVA POWER</span>
  </div>
  <div class="btn quote">Free Quote</div>
  <div class="contact-item" style="left:700px;top:14px">
    <svg width="16" height="16" viewBox="0 0 16 16"><path d="M1 8 15 1 11 15 8 9Z" fill="#fff"/></svg>
    <div><div class="big">(07) 3000 4815</div><div class="small">torvapower@mailbox.com</div></div>
  </div>
  <div class="contact-item" style="left:920px;top:14px">
    <svg width="14" height="18" viewBox="0 0 14 18"><path d="M7 0a7 7 0 0 1 7 7c0 5-7 11-7 11S0 12 0 7a7 7 0 0 1 7-7Z" fill="#fff"/><circle cx="7" cy="7" r="2.6" fill="#262626"/></svg>
    <div><div class="big">48-52 Wattle</div><div class="small">Lane Kelbrook QLD 4130</div></div>
  </div>
</header>

<nav class="main-nav">
  <span style="left:681px">HOME</span>
  <span style="left:778px">RESIDENTIAL</span>
  <span style="left:913px">COMMERCIAL</span>
  <span style="left:1052px">OFF-GRID</span>
</nav>

<section class="hero">
  <div class="photo hero-photo" role="img" aria-label="Aerial view of suburban homes with rooftop solar panels beside the water"></div>
  <div class="hero-shade"></div>
  <form class="abs quote-form">
    <h3>FREE NO OBLIGATION QUOTE!</h3>
    <div class="sub">Get a FREE customized Quote for your Home or Business!</div>
    <div class="field" style="top:80px">Name:<div class="box"></div></div>
    <div class="field" style="top:130px">Email:<div class="box"></div></div>
    <div class="field" style="top:180px">Phone:<div class="box"></div></div>
    <div class="field" style="top:229px">Postcode:<div class="box"></div></div>
    <div class="field" style="top:279px">Message:<div class="box" style="height:72px"></div></div>
    <div class="btn outline">Get Free Quote</div>
  </form>
  <div class="abs hero-copy">
    <div class="kicker">TIRED OF THE POWER BILL</div>
    <h1>GETTING LARGER<br>EACH YEAR?</h1>
    <p>Torva Power is Australia's top provider and authority in solar &amp; off-grid energy solutions. We're here to help you save up to 80% on your energy costs through our effective and efficient energy management systems!</p>
  </div>
</section>

<section class="welcome">
  <div class="abs kicker">WELCOME TO</div>
  <h2 class="abs">TORVA POWER</h2>
  <p class="abs">High quality customised energy solutions Off grid Solar installations Solar PV Installations Commercial Energy Management Solutions<br>At Torva Power we focus on our most important asset, you the customer. We understand that not every business or home has the same energy requirements. That is why we develop individual solutions tailored to meet the needs of each and every customer. It is our commitment to provide exceptional value to our customers by offering all available renewable energy solutions through our custom designed solutions.</p>
  <div class="btn">Read More</div>
  <div class="photo welcome-photo" role="img" aria-label="Aerial photo of a modern house with a solar panel array on its roof"></div>
</section>

<section class="services">
  <div class="card" style="left:93px">
    <i class="c-tl"></i><i class="c-br"></i>
    <svg width="40" height="40" viewBox="0 0 40 40" fill="none" stroke="#d9262f" stroke-width="1.8"><circle cx="20" cy="20" r="8"/><path d="M20 3v6M20 31v6M3 20h6M31 20h6M8 8l4 4M28 28l4 4M8 32l4-4M28 12l4-4"/></svg>
    <div class="label">Commercial Solar Power</div>
    <h3>Reduce Costs, Grow Your Business</h3>
    <p>If you're running a business, then our Commercial Energy Solutions are perfectly suited for your power-intensive operations!</p>
  </div>
  <div class="card" style="left:352px">
    <i class="c-tl"></i><i class="c-br"></i>
    <svg width="40" height="40" viewBox="0 0 40 40" fill="none" stroke="#d9262f" stroke-width="1.8"><path d="M6 18h28l-3-10H9Z M14 8v10M20 8v10M26 8v10M7 13h26M20 18v16M12 34h16"/></svg>
    <div class="label">Off Grid Power</div>
    <h3>Avoid Blackouts, Go Off-Grid</h3>
    <p>In a country where blackouts and power outages are all too common, our Off Grid Power Solutions can make your electricity more dependable to avoid disruption in your operations.</p>
  </div>
  <div class="card raised" style="left:611px">
    <i class="c-tl"></i><i class="c-br" style="border-color:var(--red)"></i>
    <svg width="40" height="40" viewBox="0 0 40 40" fill="none" stroke="#d9262f" stroke-width="1.8"><rect x="8" y="4" width="24" height="12"/><path d="M14 4v12M20 4v12M26 4v12M20 16v6"/><rect x="10" y="22" width="20" height="14"/><path d="M10 29H4M30 29h6"/></svg>
    <div class="label">Solar Water Pumps</div>
    <h3>Go Solar, Eliminate Fuel Cost</h3>
    <p>We know you want to grow so we help you find more cost-efficient alternatives versus expensive traditional options such as fossil fuel water pumps.</p>
  </div>
  <div class="card" style="left:870px">
    <i class="c-tl"></i><i class="c-br"></i>
    <svg width="40" height="40" viewBox="0 0 40 40" fill="none" stroke="#d9262f" stroke-width="1.8"><path d="M4 20 20 6l16 14M9 16v18h22V16"/><rect x="15" y="20" width="10" height="8"/><path d="M20 20v8M15 24h10"/></svg>
    <div class="label">Residential Solar Power</div>
    <h3>Save Money For Your Family</h3>
    <p>Our Residential Solar Power solutions can give you up to 80% reduction on your power bills — allowing you to save money for the future use of your family!</p>
  </div>
</section>

<section class="promo">
  <div class="photo promo-art" role="img" aria-label="Illustration of a house with rooftop solar panels among trees on a green hill"></div>
  <div class="abs kicker">TORVA POWER CUT 80% OFF</div>
  <h2 class="abs">THEIR POWER BILL</h2>
  <p class="abs" style="top:176px">Whether you're a huge commercial establishment or a simple property owner, Torva Power has the perfect solution to give you consistent savings on your monthly bills.</p>
  <p class="abs" style="top:246px">Get your FREE Quote and discover how you can save thousands of dollars from reduced energy cost by choosing to go solar!</p>
  <div class="btn outline">Get A Free Quote</div>
</section>

<section class="why">
  <svg class="abs" style="left:1090px;top:138px" width="110" height="460" viewBox="0 0 110 460"><polygon points="110,0 110,460 0,170" fill="#d9262f"/></svg>
  <svg class="abs" style="left:0;top:812px" width="110" height="367" viewBox="0 0 110 367"><polygon points="0,0 108,265 0,367" fill="#d9262f"/></svg>
  <div class="abs kicker">WHY DO YOU</div>
  <h2 class="abs">NEED TO GO SOLAR?</h2>

  <div class="reason" style="left:601px;top:200px">
    <svg width="56" height="56" viewBox="0 0 56 56" fill="none" stroke="#d9262f" stroke-width="2"><rect x="4" y="8" width="26" height="8" rx="2"/><rect x="4" y="18" width="26" height="8" rx="2"/><rect x="4" y="28" width="26" height="8" rx="2"/><circle cx="38" cy="34" r="14"/><path d="M38 26v16M34 30h6a3 3 0 0 1 0 6h-4a3 3 0 0 0 0 6h6"/></svg>
    <div class="kick">GET CONSISTENT</div>
    <h3>SAVINGS FOR 20+ YEARS</h3>
    <p>We can't deny that the cost of electricity is consistently rising. And whether you're a commercial organisation or a simple homeowner, dealing with high expensive energy costs can be a real struggle.</p>
  </div>
  <div class="reason" style="left:93px;top:342px">
    <svg width="56" height="56" viewBox="0 0 56 56" fill="none" stroke="#d9262f" stroke-width="2"><circle cx="28" cy="14" r="6"/><path d="M28 2v3M18 6l2 3M38 6l-2 3M6 24l12 14h10M50 24 38 38H28M10 34v18M46 34v18"/></svg>
    <div class="kick">BE INDEPENDENT</div>
    <h3>FROM THE GRID</h3>
    <p>Gone are the days when the only way to use electricity is through the grid. Now, you don't have to suffer from expensive electricity costs and terrible service. You now have the power to go off-grid and reduce your electricity costs!</p>
  </div>
  <div class="reason" style="left:601px;top:510px">
    <svg width="56" height="56" viewBox="0 0 56 56" fill="none" stroke="#d9262f" stroke-width="2"><path d="M4 52h48M8 52V38h8v14M20 52V30h8v14M32 52V24h8v28M44 52V16h8v36M6 30 22 18l10 6 18-16M42 8h8v8"/></svg>
    <div class="kick">INCREASE AND MAXIMISE</div>
    <h3>YOUR BOTTOMLINE</h3>
    <p>Saving money on electricity costs is only half of the equation. The money you save can be used on other revenue-generating activities. Combining this will result in maximising your profits and increasing your bottomline. Giving you more 'power' to reach new heights for your business!</p>
  </div>
  <div class="reason" style="left:93px;top:672px">
    <svg width="56" height="56" viewBox="0 0 56 56" fill="none" stroke="#d9262f" stroke-width="2"><circle cx="26" cy="30" r="22"/><circle cx="26" cy="30" r="14"/><circle cx="26" cy="30" r="6"/><path d="M26 30 50 6M44 6h6v6"/></svg>
    <div class="kick">DIFFERENTIATE YOUR BUSINESS</div>
    <h3>AGAINST COMPETITORS</h3>
    <p>With the increasing awareness of people with regards to global warming, being an organisation who supports renewable energy initiatives is a huge brand differentiator. Be an advocate of clean energy. Reduce emissions footprint and enjoy the favor of your prospects and loyalty of your customers.</p>
  </div>
  <div class="reason" style="left:601px;top:852px">
    <svg width="56" height="56" viewBox="0 0 56 56" fill="none" stroke="#d9262f" stroke-width="2"><circle cx="28" cy="28" r="24"/><ellipse cx="28" cy="28" rx="11" ry="24"/><path d="M4 28h48M8 16h40M8 40h40"/></svg>
    <div class="kick">TAKE PART IN SOLVING</div>
    <h3>GLOBAL WARMING</h3>
    <p>Solar energy is clean, renewable and sustainable. Unlike using fossil fuels, solar energy can reduce your carbon footprint and harmful greenhouse gas emissions. And if your company stands to protect the environment, then using solar energy is a no-brainer!</p>
  </div>
</section>

<section class="plug">
  <h2 class="abs">PLUG INTO THE SUN.</h2>
  <p class="abs">At Torva Power, we believe that you deserve better. Poor services and huge costs for electricity don't sit well with us. That's why we do our best to provide our clients with up-to-date energy management systems that can immediately result to significant reductions in their electricity expenses.</p>
  <div class="btn">Read More</div>
  <div class="photo" style="left:93px;top:342px;width:245px;height:179px;background:linear-gradient(180deg,#aac9e6 0%,#c8dbea 35%,#4a4e55 60%,#6d7266 100%)" role="img" aria-label="House with dark roof and solar panels"></div>
  <div class="photo" style="left:348px;top:342px;width:247px;height:179px;background:linear-gradient(180deg,#b7d4ee 0%,#d6e4ef 30%,#2f3a52 55%,#6e7880 100%)" role="img" aria-label="Close view of rooftop solar panel rows"></div>
  <div class="photo" style="left:634px;top:77px;width:471px;height:444px;background:linear-gradient(135deg,#8d8b88 0%,#c9c7c3 40%,#e8e6e2 60%,#8a8885 100%)" role="img" aria-label="Wall-mounted solar inverter with cabling"></div>
</section>

<section class="articles">
  <div class="article" style="left:93px">
    <div class="photo pic" style="position:relative;background:linear-gradient(180deg,#5c6b4e 0%,#8c9478 35%,#b7b9b5 55%,#39445a 100%)" role="img" aria-label="Large shed roof covered with solar panels beside farmland"></div>
    <h3>A More Cost-Efficient Alternative To Your Irrigation Needs</h3>
    <p>Conventional water pump systems can be quite costly. Volatile prices of fuel and other related expenses contribute to adding massive burden to your operations. Torva Power offers you a more cost-efficient alternative through our solar water pumps. Now, increasing your efficiency while reducing your costs is possible!</p>
  </div>
  <div class="article" style="left:614px">
    <div class="photo pic" style="position:relative;background:linear-gradient(180deg,#8fb8e0 0%,#b5cfe6 25%,#6c7a6a 45%,#2c3850 100%)" role="img" aria-label="Rows of solar panels on a suburban rooftop under blue sky"></div>
    <h3>Add Thousands of Dollars to Your Bottomline!</h3>
    <p>Torva Power has a full range of energy management solutions that will help your business reduce energy costs. In addition, we will also help you in maximising all available tax deductions while shortening your payback period. The overall result? Thousands of dollars added to your bottomline!</p>
  </div>
</section>

<section class="testimonials">
  <div class="abs kicker">HERE'S WHAT OUR</div>
  <h2 class="abs">CLIENTS ARE SAYING</h2>
  <div class="quote" style="left:116px">
    <div class="avatar" role="img" aria-label="Portrait photo of client Helena"></div>
    <p>Have been a pleasure to deal with and came up with a combinations of ideas to save money</p>
    <div class="who">Helena</div>
    <div class="role">Client</div>
  </div>
  <div class="quote" style="left:622px">
    <div class="avatar" role="img" aria-label="Portrait photo of client Marcus"></div>
    <p>My new solar water pump hasn't missed a beat and have saved me a fortune in diesel fuel</p>
    <div class="who">Marcus</div>
    <div class="role">Client</div>
  </div>
</section>

<section class="partners" aria-label="Partner brands">
  <div class="badge" style="left:128px;width:136px"></div>
  <div class="badge" style="left:330px;width:136px"></div>
  <div class="badge" style="left:553px;width:92px;border-radius:28px"></div>
  <div class="badge" style="left:727px;width:150px"></div>
  <div class="badge" style="left:960px;width:92px;background:#444"></div>
</section>

<footer class="site-footer">
  <div class="col" style="left:93px">
    <h4>Sitemap</h4>
    <ul><li>Home</li><li>Residential</li><li>Commercial</li><li>Off Grid</li><li>Contact Us</li></ul>
  </div>
  <div class="col" style="left:316px">
    <h4>What We Do</h4>
    <ul><li>Commercial Solar Power</li><li>Off Grid Power</li><li>Solar Water Pump</li><li>Residential Solar Power</li></ul>
  </div>
  <div class="abs contact-box">
    <div class="col" style="left:28px;top:62px">
      <h4>Contact Us</h4>
      <div class="row"><svg width="9" height="12" viewBox="0 0 14 18"><path d="M7 0a7 7 0 0 1 7 7c0 5-7 11-7 11S0 12 0 7a7 7 0 0 1 7-7Z" fill="#fff"/></svg><span>48-52 Wattle Lane Kelbrook QLD 4130</span></div>
      <div class="row"><svg width="11" height="11" viewBox="0 0 16 16"><path d="M3 1h3l2 4-2 2a9 9 0 0 0 3 3l2-2 4 2v3c0 1-1 2-2 2A13 13 0 0 1 1 3c0-1 1-2 2-2Z" fill="#fff"/></svg><span>(07) 3000 4815</span></div>
      <div class="row"><svg width="11" height="9" viewBox="0 0 16 12"><rect width="16" height="12" fill="#fff"/><path d="M0 0l8 7 8-7" stroke="#d9262f" fill="none"/></svg><span>torvapower@mailbox.com</span></div>
    </div>
  </div>
  <div class="col" style="left:955px">
    <h4>Opening Hours</h4>
    <div style="color:#fff">Monday - Friday:</div>
    <div>9:00AM - 5:00PM</div>
    <div style="color:#fff;font-family:Montserrat,sans-serif;margin-top:24px;font-size:12px">FOLLOW US ON</div>
    <div style="display:flex;gap:8px;margin-top:10px"><i class="dot" style="width:11px;height:11px"></i><i class="dot" style="width:11px;height:11px"></i><i class="dot" style="width:11px;height:11px"></i><i class="dot" style="width:11px;height:11px"></i></div>
  </div>
  <div class="abs copy">COPYRIGHT © 2019 <b>TORVA POWER</b>. ALL RIGHTS RESERVED.</div>
</footer>

</body>
</html>
```